Revamping MarcelTouvier.com like a portal of all services

I have my website marceltouvier.com that is about my trading school.
I have bluemarketix.com for my currencies strategies,
I have mt-vault.com for my crypto strategy.

I would like to regroup all under marceltouvier.com by revamping all this website in one brand new

1-Color code under mt-vault.com
2-All my 3 services on different one pager connected to the home page.
3-Need attractive website. Any disruptive feature is welcome.

The website should be a portal resuming all the activities of Marcel Touvier as described below:

Page 1 :
Home Page presenting the 3 services of marcel touvier

Page 2 :
One pager presenting https://bluemarketix.com

Page 3:
One pager presenting https://mt-vault.com

Page 4:
One pager presenting https://marceltouvier.com/leafkey/

Page 5:
Page for faq and contact

Target Market(s)

Financial investors

Industry/Entity Type

Finance Crypto

Coding

Coded - Design and coding required

Number of Pages Required

5+ page

Requirements
Must have
• Financial elements
Nice to have
• Animated element

```html
<!DOCTYPE html>
<html lang="en">
<head>
<meta charset="utf-8">
<title>Marcel Touvier — Trading Portal</title>
<link href="https://fonts.googleapis.com/css2?family=Raleway:wght@400;500;600;700;800;900&family=Nunito:wght@400;600;700&display=swap" rel="stylesheet">
<style>
:root{
  --purple:#4a2184;
  --purple-deep:#371270;
  --purple-top:#5a2c8e;
  --violet:#8a4bd8;
  --orange:#f5721f;
  --sky:#3ea3f2;
  --ink:#1e1e24;
  --text:#555a64;
  --link:#1a7ae0;
  --footer:#1d1d1f;
  --white:#ffffff;
}
*{box-sizing:border-box;margin:0;padding:0}
html,body{width:1200px;height:3161px;overflow:hidden}
body{font-family:"Nunito",sans-serif;color:var(--ink);background:var(--white)}
a{color:inherit;text-decoration:none}
.wrap{position:relative;width:940px;margin:0 auto;height:100%}
section,header,footer,nav{position:relative;width:1200px}

/* top bar */
.topbar{height:27px;background:var(--purple-top);color:#fff}
.topbar .wrap{display:flex;align-items:center;justify-content:space-between}
.socials{display:flex;gap:21px;padding-left:2px}
.socials span{width:13px;height:13px;border-radius:50%;background:#fff;opacity:.9}
.top-phone{display:flex;align-items:center;gap:7px;font-size:11px;font-family:"Raleway",sans-serif;font-weight:500}
.top-phone i{width:22px;height:22px;border-radius:50%;background:#fff;display:flex;align-items:center;justify-content:center}

/* nav */
.nav{height:50px;background:#fff;box-shadow:0 1px 0 #eee}
.nav .wrap{display:flex;align-items:center;justify-content:space-between}
.brand{font-family:"Raleway",sans-serif;font-weight:700;font-size:21px;color:var(--ink)}
.menu{display:flex;gap:44px;font-family:"Raleway",sans-serif;font-weight:600;font-size:13px;color:#111}
.menu a.active{color:var(--violet);text-decoration:underline;text-underline-offset:4px}

/* hero */
.hero{height:431px;background:linear-gradient(100deg,#34106e 0%,#3c1780 45%,#46208e 100%);overflow:hidden;color:#fff}
.hero-chart{position:absolute;inset:0;background:linear-gradient(180deg,rgba(80,60,170,.25),rgba(40,20,100,.1) 60%,rgba(120,40,80,.25))}
.hero-portrait{position:absolute;left:577px;top:0;width:490px;height:431px;background:radial-gradient(ellipse at 50% 35%,#c99a84 0%,#8c6a80 22%,#3b3d8c 52%,rgba(60,40,140,0) 75%)}
.hero-text{position:absolute;left:0;top:99px}
.hero-kicker{font-family:"Raleway",sans-serif;font-size:20px;font-weight:500}
.hero-title{font-family:"Raleway",sans-serif;font-weight:900;font-size:56px;line-height:64px;margin-top:10px;letter-spacing:-1px;text-transform:uppercase}
.hero-title em{font-style:normal;color:var(--sky)}
.btn-orange{display:inline-block;margin-top:22px;background:var(--orange);color:#fff;font-family:"Raleway",sans-serif;font-weight:600;font-size:14.5px;height:47px;line-height:47px;width:269px;text-align:center}

/* about */
.about{height:497px}
.about-photo-a{position:absolute;left:0;top:56px;width:239px;height:280px;background:linear-gradient(160deg,#5b6068,#9aa0a6 55%,#d8dadc)}
.about-tile{position:absolute;left:239px;top:92px;width:81px;height:50px;background:#f1f1f1}
.about-photo-b{position:absolute;left:188px;top:146px;width:271px;height:287px;background:linear-gradient(170deg,#d9b58a 0%,#b6c2d8 35%,#3c4a66 70%,#2a2a33)}
.about-text{position:absolute;left:560px;top:145px;width:380px}
.about-text small{font-family:"Raleway",sans-serif;font-size:17px;font-weight:500}
.about-text h2{font-family:"Raleway",sans-serif;font-weight:700;font-size:34px;margin-top:2px}
.about-text p{font-size:14.5px;line-height:22px;margin-top:12px;color:#222}
.btn-purple{display:inline-block;background:var(--purple);color:#fff;font-family:"Raleway",sans-serif;font-weight:500;font-size:12px;width:111px;height:36px;line-height:36px;text-align:center}
.about-text .btn-purple{margin-top:21px}

/* services */
.services{height:476px;background:radial-gradient(ellipse at 15% 40%,#1f3a4a 0%,rgba(20,26,56,0) 45%),linear-gradient(180deg,#10193a,#141c3c 60%,#0e1530)}
.section-title{font-family:"Raleway",sans-serif;font-weight:700;font-size:34px;text-align:center}
.services .section-title{color:#fff;padding-top:43px}
.cards{position:absolute;left:0;top:105px;display:flex;gap:20px}
.card{width:300px;height:322px;background:#fff;text-align:center;padding-top:36px}
.card-logo{height:80px;display:flex;flex-direction:column;align-items:center;justify-content:center;gap:9px}
.card-logo .dot{width:38px;height:38px;border-radius:50%;background:var(--purple)}
.card-logo .name{font-family:"Raleway",sans-serif;font-weight:600;font-size:15px;color:var(--ink)}
.card h3{font-family:"Raleway",sans-serif;font-weight:500;font-size:19px;margin-top:36px}
.card p{font-size:12.5px;line-height:18px;color:var(--text);margin:14px 20px 0}
.card a{display:inline-block;margin-top:14px;font-size:12.5px;color:var(--link);text-decoration:underline}

/* features */
.features{height:431px}
.feat-grid{position:absolute;left:0;top:60px;display:flex;gap:20px}
.feat{width:220px;height:312px;text-align:center;padding-top:39px}
.feat.hl{background:var(--purple-deep);color:#fff;padding-top:22px}
.feat .ico{width:100px;height:100px;border-radius:50%;margin:0 auto;background:linear-gradient(135deg,#6a2fa8,#3a1474);display:flex;align-items:center;justify-content:center}
.feat.hl .ico{background:#fff}
.feat.low{padding-top:49px}
.feat h3{font-family:"Raleway",sans-serif;font-weight:500;font-size:20px;margin-top:20px}
.feat p{font-size:11.5px;line-height:17.5px;color:var(--text);margin:10px 18px 0}
.feat.hl p{color:#fff}

/* contact */
.contact{height:386px;background:linear-gradient(120deg,#2c2e3a 0%,#3a3f52 35%,#262a38 70%,#33384a);color:#fff}
.contact .section-title{padding-top:82px;color:#fff}
.form{position:absolute;left:149px;top:142px;width:640px}
.row{display:flex;gap:7px}
.field{background:#fff;color:#222;font-size:10.5px;height:43px;padding:17px 14px 0;flex:1}
.field.msg{height:81px;margin-top:7px}
.submit{margin-top:11px;height:35px;background:var(--purple);color:#fff;text-align:center;line-height:35px;font-family:"Raleway",sans-serif;font-weight:600;font-size:12px}

/* blog */
.blog{height:514px}
.blog .section-title{padding-top:47px}
.posts{position:absolute;left:0;top:107px;display:flex;gap:20px}
.post{width:300px;position:relative}
.post-img{height:184px}
.img-1{background:linear-gradient(135deg,#d8cba5,#8c7f6a 45%,#1c2a3e 70%,#3a4fa0)}
.img-2{background:linear-gradient(135deg,#f2f3f5,#c9ccd2 50%,#6c707a)}
.img-3{background:linear-gradient(135deg,#7a5a2a,#c9a24a 30%,#1b2638 55%,#0f1a2c)}
.pill{position:absolute;left:5px;top:168px;width:78px;height:28px;border-radius:14px;background:var(--orange);color:#fff;font-size:11.5px;font-weight:700;text-align:center;line-height:28px}
.post h3{font-family:"Raleway",sans-serif;font-weight:500;font-size:17px;margin-top:35px}
.post p{font-size:12px;line-height:18px;color:var(--text);margin-top:9px;height:54px}
.post .btn-purple{margin-top:14px}

/* footer */
.footer{height:349px;background:var(--footer);color:#fff}
.f-brand{position:absolute;left:0;top:54px;font-family:"Raleway",sans-serif;font-weight:700;font-size:32px;color:#fff}
.f-about{position:absolute;left:0;top:108px;width:310px;font-size:12px;line-height:20px;font-weight:600}
.f-social{position:absolute;left:0;top:215px;display:flex;gap:10px}
.f-social span{width:28px;height:28px;border-radius:50%;border:1.5px solid #fff}
.f-col{position:absolute;top:60px}
.f-col h4{font-family:"Raleway",sans-serif;font-weight:600;font-size:19px}
.f-col ul{list-style:none;margin-top:8px}
.f-col li{font-size:11.5px;height:24.6px;line-height:24.6px}
.col-1{left:384px}.col-2{left:547px}.col-3{left:732px}
.divider{position:absolute;top:59px;width:1px;height:166px;background:#3a3a3e}
.contact-item{display:flex;gap:10px;font-size:11.5px;line-height:13px;margin-top:12px;align-items:flex-start}
.contact-item i{flex:none;width:26px;height:26px;border-radius:50%;background:var(--purple);display:flex;align-items:center;justify-content:center}
.contact-item span{padding-top:3px}
.copyright{position:absolute;left:0;right:0;top:282px;text-align:center;font-size:10px;color:#8a8a8e}
.copyright b{color:#fff;font-weight:400}
</style>
</head>
<body>

<header class="topbar">
  <div class="wrap">
    <div class="socials" aria-label="Social profiles"><span></span><span></span><span></span><span></span><span></span></div>
    <div class="top-phone">
      <i><svg width="11" height="11" viewBox="0 0 24 24"><path fill="#5a2c8e" d="M6.6 10.8a15 15 0 0 0 6.6 6.6l2.2-2.2c.3-.3.7-.4 1-.2 1.1.4 2.3.6 3.6.6.6 0 1 .4 1 1V20c0 .6-.4 1-1 1A17 17 0 0 1 3 4c0-.6.4-1 1-1h3.5c.6 0 1 .4 1 1 0 1.3.2 2.5.6 3.6.1.3 0 .7-.2 1z"/></svg></i>
      +2 (555) 240 7300
    </div>
  </div>
</header>

<nav class="nav">
  <div class="wrap">
    <div class="brand">Marcel Touvier</div>
    <div class="menu">
      <a class="active">Home</a><a>Leaf Key</a><a>Contact me</a><a>Student Area</a><a>Blog</a><a>FAQ</a>
    </div>
  </div>
</nav>

<section class="hero">
  <div class="hero-chart" role="img" aria-label="Background of trading screens with candlestick charts and a dashboard"></div>
  <div class="wrap">
    <div class="hero-portrait" role="img" aria-label="Portrait photo of Marcel Touvier in a blue shirt"></div>
    <div class="hero-text">
      <div class="hero-kicker">The World’s Most Popular</div>
      <h1 class="hero-title">FX Trader in<br><em>Social</em> Trading</h1>
      <a class="btn-orange">DISCOVER MY TRADING SCHOOL</a>
    </div>
  </div>
</section>

<section class="about">
  <div class="wrap">
    <div class="about-photo-a" role="img" aria-label="Gloved hand holding a smartphone with a trading app"></div>
    <div class="about-tile"></div>
    <div class="about-photo-b" role="img" aria-label="Marcel Touvier seated in front of trading monitors"></div>
    <div class="about-text">
      <small>About</small>
      <h2>Marcel Touvier</h2>
      <p>Contact me to know more about all of my different activities including coaching, asset management and trading systems. This will simply change your life.</p>
      <a class="btn-purple">Contact Me</a>
    </div>
  </div>
</section>

<section class="services">
  <div class="wrap">
    <h2 class="section-title">Our Services</h2>
    <div class="cards">
      <div class="card">
        <div class="card-logo"><span class="dot"></span><span class="name">Marcel Touvier</span></div>
        <h3>Trading School</h3>
        <p>Sed ut perspiciatis unde omnis iste natus error sit voluptatem accusantium doloremque laudantium, totam rem aperiam, eaque ipsa quae ab illo inventore veritatis et quasi architecto</p>
        <a>marceltouvier.com</a>
      </div>
      <div class="card">
        <div class="card-logo"><span class="dot"></span><span class="name">Marcel Touvier FUND</span></div>
        <h3>Currencies Sstrategies</h3>
        <p>Sed ut perspiciatis unde omnis iste natus error sit voluptatem accusantium doloremque laudantium, totam rem aperiam, eaque ipsa quae ab illo inventore veritatis et quasi architecto</p>
        <a>bluemarketix.com</a>
      </div>
      <div class="card">
        <div class="card-logo"><span class="dot"></span><span class="name">BlueMarketix</span></div>
        <h3>Crypto Strategy</h3>
        <p>Sed ut perspiciatis unde omnis iste natus error sit voluptatem accusantium doloremque laudantium, totam rem aperiam, eaque ipsa quae ab illo inventore veritatis et quasi architecto</p>
        <a>mt-vault.com</a>
      </div>
    </div>
  </div>
</section>

<section class="features">
  <div class="wrap">
    <div class="feat-grid">
      <div class="feat">
        <div class="ico"><svg width="44" height="44" viewBox="0 0 44 44" fill="none" stroke="#fff" stroke-width="3.5"><circle cx="18" cy="18" r="12"/><path d="M27 27l11 11" stroke-linecap="round"/><path d="M13 22v-4M18 22v-8M23 22v-5" stroke-width="3"/></svg></div>
        <h3>Past Analysis</h3>
        <p>I am taking into consideration the personal history of each student so that I can adapt my teaching methods for you to have a better experience in trading.</p>
      </div>
      <div class="feat hl">
        <div class="ico"><svg width="48" height="44" viewBox="0 0 48 44" fill="none" stroke="#4a2184" stroke-width="2.5"><rect x="16" y="4" width="28" height="20"/><path d="M22 18l5-5 4 3 7-7"/><circle cx="8" cy="8" r="4" fill="#4a2184"/><path d="M4 26v-8h8l6 4"/><circle cx="14" cy="32" r="3" fill="#4a2184"/><circle cx="24" cy="32" r="3" fill="#4a2184"/><circle cx="34" cy="32" r="3" fill="#4a2184"/><path d="M9 42c0-4 10-4 10 0M19 42c0-4 10-4 10 0M29 42c0-4 10-4 10 0"/></svg></div>
        <h3>Coaching Classes</h3>
        <p>There will be weekly sessions from an upstream questionnaire and a ‘basics session’ with an explanation of the tools and methods. There will be training exercises until a final adjustment session.</p>
      </div>
      <div class="feat low">
        <div class="ico"><svg width="46" height="46" viewBox="0 0 46 46" fill="none" stroke="#fff" stroke-width="3.5" stroke-linecap="round"><path d="M38 18A16 16 0 0 0 9 13"/><path d="M8 5v9h9"/><path d="M8 28a16 16 0 0 0 29 5"/><path d="M38 41v-9h-9"/></svg></div>
        <h3>Trading Dashboard</h3>
        <p>You will have all the necessary tools to better understand the market movement and know how to detect opportunities.</p>
      </div>
      <div class="feat">
        <div class="ico"><svg width="40" height="46" viewBox="0 0 40 46"><circle cx="20" cy="13" r="9" fill="#fff"/><path d="M3 44c0-12 8-18 17-18s17 6 17 18z" fill="#fff"/><path d="M20 27l-3 5 3 9 3-9z" fill="#4a2184"/></svg></div>
        <h3>A New Person</h3>
        <p>You will obviously be transformed in the way you think, both in your trading activity and your personal life. You will feel the improvements on a daily basis.</p>
      </div>
    </div>
  </div>
</section>

<section class="contact" role="img" aria-label="Dimmed background of hands typing on a laptop">
  <div class="wrap">
    <h2 class="section-title">Get in Touch</h2>
    <div class="form">
      <div class="row"><div class="field">Name:</div><div class="field">Email:</div></div>
      <div class="field msg">Message:</div>
      <div class="submit">Submit</div>
    </div>
  </div>
</section>

<section class="blog">
  <div class="wrap">
    <h2 class="section-title">Recent Blog</h2>
    <div class="posts">
      <article class="post">
        <div class="post-img img-1" role="img" aria-label="Tablet showing a trading chart next to a bowl of candy"></div>
        <span class="pill">June 30</span>
        <h3>EURUSD Trade with Leaf Key</h3>
        <p>Let’s see how my last $EURUSD was managed. I have a lot of questions about my strategies, here is an explanation of this trade which</p>
        <a class="btn-purple">Read More</a>
      </article>
      <article class="post">
        <div class="post-img img-2" role="img" aria-label="Desk with printed charts, a magnifier and glasses"></div>
        <span class="pill">Feb 25</span>
        <h3>First look of Forex correlation (part 1)</h3>
        <p>All FX assets move mainly on technical and fundamental events. Most people either do not understand or simply ignore that fact...</p>
        <a class="btn-purple">Read More</a>
      </article>
      <article class="post">
        <div class="post-img img-3" role="img" aria-label="Crypto coins in front of a market chart screen"></div>
        <span class="pill">Dec 29</span>
        <h3>Avoid Overtrading</h3>
        <p>Overtrading is a little-known but often overlooked problem for everyone in the business, but especially day traders and scalpers.</p>
        <a class="btn-purple">Read More</a>
      </article>
    </div>
  </div>
</section>

<footer class="footer">
  <div class="wrap">
    <div class="f-brand">Marcel Touvier</div>
    <p class="f-about">Learn and get all the tools to be a better trader, Improve your skills to be regular in your trading, detect opportunities on the markets with easy to replicate strategies.</p>
    <div class="f-social" aria-label="Social profiles"><span></span><span></span><span></span><span></span><span></span></div>

    <div class="f-col col-1"><h4>Sitemap</h4><ul><li>Home</li><li>Leaf Key</li><li>Contact me</li><li>Student Area</li><li>Blog'</li><li>FAQ</li></ul></div>
    <div class="divider" style="left:506px"></div>
    <div class="f-col col-2"><h4>Others Link</h4><ul><li>My Tradevia profile</li><li>Terms &amp; Conditons</li><li>Privacy Policy</li><li>Cookies Policy</li><li>Copy Right Policy</li></ul></div>
    <div class="divider" style="left:691px"></div>
    <div class="f-col col-3"><h4>Contacts</h4>
      <div class="contact-item"><i><svg width="10" height="13" viewBox="0 0 10 13"><path fill="#fff" d="M5 0a5 5 0 0 0-5 5c0 4 5 8 5 8s5-4 5-8a5 5 0 0 0-5-5zm0 7a2 2 0 1 1 0-4 2 2 0 0 1 0 4z"/></svg></i><span>15K Lorem ipsum dolar sit amet<br>Glassglow 250 UKE</span></div>
      <div class="contact-item" style="margin-top:24px"><i><svg width="11" height="11" viewBox="0 0 24 24"><path fill="#fff" d="M6.6 10.8a15 15 0 0 0 6.6 6.6l2.2-2.2c.3-.3.7-.4 1-.2 1.1.4 2.3.6 3.6.6.6 0 1 .4 1 1V20c0 .6-.4 1-1 1A17 17 0 0 1 3 4c0-.6.4-1 1-1h3.5c.6 0 1 .4 1 1 0 1.3.2 2.5.6 3.6.1.3 0 .7-.2 1z"/></svg></i><span>+2 (555) 240 7300</span></div>
      <div class="contact-item" style="margin-top:24px"><i><svg width="12" height="9" viewBox="0 0 12 9"><rect width="12" height="9" rx="1" fill="#fff"/><path d="M0 1l6 4 6-4" stroke="#4a2184" fill="none"/></svg></i><span>contact@marceltouvier.com</span></div>
    </div>

    <div class="copyright">Copyright © 2022 <b>Marcel Touvier</b>. All Rights Reserved.</div>
  </div>
</footer>

</body>
</html>
```